Home care agency

Current website QRVCAREPLUS.com. Need to update and reformat to different pages. use my info from my current website

Target Market(s)

adult children

Industry/Entity Type

Home Health

Coding

Coded - Design and coding required

Number of Pages Required

4 page

Font styles to use
Sans Serif

Colors
3276b5
33a6d7
3277b5
85cae6
85acd3

```html
<!DOCTYPE html>
<html lang="en">
<head>
<meta charset="utf-8">
<title>Harbor Light Home Health &amp; Home Services</title>
<link href="https://fonts.googleapis.com/css2?family=Lato:ital,wght@0,400;0,700;1,400&family=Playfair+Display:ital,wght@0,700;1,400&display=swap" rel="stylesheet">
<style>
:root{
  --blue:#3276b5;
  --sky:#33a6d7;
  --pale:#85cae6;
  --soft:#85acd3;
  --teal:#8fd4c8;
  --hero:#a8ddd5;
  --mist:#f1f6fa;
  --light-col:#cfe8f5;
  --ink:#1f2326;
  --text:#3d4247;
  --muted:#8a9096;
  --footer:#262626;
  --footer-deep:#1b1b1b;
  --serif:'Playfair Display', Georgia, serif;
  --sans:'Lato', Arial, sans-serif;
}
*{margin:0;padding:0;box-sizing:border-box}
html,body{width:1200px;height:3947px;overflow:hidden}
body{position:relative;background:#fff;font-family:var(--sans);color:var(--text)}
.abs{position:absolute}
a{color:inherit;text-decoration:none}

/* header */
.topbar{left:0;top:0;width:1200px;height:75px;background:#fff}
.navband{left:0;top:75px;width:1200px;height:52px;background:#eef4f8}
.brand-box{left:234px;top:0;width:158px;height:158px;background:#fff;box-shadow:0 2px 8px rgba(0,0,0,.08);z-index:5;display:flex;flex-direction:column;align-items:center;justify-content:center;gap:8px}
.brand-box .dot{width:14px;height:14px;border-radius:50%;background:var(--pale)}
.brand-name{font-family:var(--serif);font-weight:700;font-size:15px;color:var(--blue);text-align:center;line-height:1.25}
.contact-item{top:27px;display:flex;align-items:center;gap:8px;font-size:11px;color:var(--ink);line-height:1.35}
.contact-item.phone{font-size:19px;left:566px;top:27px}
.nav{left:458px;top:98px;display:flex;font-size:10px;font-weight:700;letter-spacing:1.2px;color:var(--ink)}
.nav span{margin-right:27px}
.btn-pill{background:var(--blue);color:#fff;border-radius:16px;font-size:9.5px;font-weight:700;letter-spacing:1.2px;display:flex;align-items:center;justify-content:center}
.inquiry-btn{left:825px;top:89px;width:137px;height:27px}

/* hero */
.hero{left:0;top:127px;width:1200px;height:360px;background:var(--hero);overflow:hidden}
.hero-photo{left:548px;top:-170px;width:666px;height:666px;border-radius:50%;background:radial-gradient(circle at 55% 45%,#e9d2c0 0,#c59f88 18%,#5a3b33 32%,#dfe4e6 50%,#f4f6f7 80%);border:6px solid #fff}
.hero-eyebrow{left:234px;top:95px;font-family:var(--serif);font-weight:700;font-size:11px;color:var(--ink)}
.hero-title{left:234px;top:115px;font-family:var(--serif);font-weight:700;font-size:40px;line-height:46px;color:var(--ink)}
.hero-btn{left:234px;top:218px;width:120px;height:26px}
.arrow{top:292px;width:22px;height:22px;border:1.5px solid #fff;border-radius:50%;color:#fff;font-size:11px;display:flex;align-items:center;justify-content:center}

/* about */
.about{left:0;top:487px;width:1200px;height:446px;background:var(--mist)}
.about-ring{left:234px;top:556px;width:320px;height:320px;border-radius:50%;background:var(--pale);display:flex;align-items:center;justify-content:center}
.about-photo{width:284px;height:284px;border-radius:50%;background:radial-gradient(circle at 45% 45%,#c8a58e 0,#7a5a4f 25%,#c9cfd3 55%,#e8ecef 100%)}
.eyebrow{font-size:10.5px;font-weight:700;letter-spacing:1.3px;color:var(--blue)}
.about-text{left:592px;top:565px;width:376px}
.about-text h2{margin-top:10px;font-family:var(--serif);font-weight:700;font-size:18.5px;line-height:26px;color:var(--ink)}
.about-text p{margin-top:16px;font-size:10.5px;line-height:16px;color:var(--ink)}
.about-text a{color:var(--blue);text-decoration:underline}

/* section headings */
.shell{width:48px;height:36px;border-radius:50% 50% 40% 40%;background:#d9ddd8}
.sec-head{left:0;width:1200px;text-align:center;font-family:var(--serif);font-weight:700;font-size:33px;letter-spacing:2px;color:var(--blue)}
.rule{width:46px;height:2px;background:var(--sky)}

/* services */
.why{left:234px;top:1140px;width:350px}
.why h3{font-family:var(--serif);font-style:italic;font-weight:400;font-size:19px;color:var(--ink);letter-spacing:.5px}
.why p{font-size:10.5px;line-height:16.5px;color:var(--ink)}
.sched{list-style:none}
.sched li{position:relative;padding-left:32px;font-size:10.5px;line-height:16.5px;color:var(--ink);margin-bottom:13px}
.sched li::before{content:"";position:absolute;left:13px;top:4px;width:6px;height:7px;border:1px solid var(--soft);border-radius:1px}
.map-title{left:640px;top:1152px;width:340px;text-align:center;font-family:var(--serif);font-style:italic;font-size:19px;color:var(--ink);letter-spacing:.5px}
.map{left:654px;top:1200px;width:314px;height:337px;border:1px solid #e3e6e8;background:linear-gradient(160deg,var(--blue) 0,var(--blue) 45%,#f6f7f8 46%,#fff 100%)}
.cols{left:234px;top:1594px;width:734px;height:250px;display:flex}
.col{flex:1;padding:24px 26px 0 27px}
.col.light{background:var(--light-col);color:var(--ink)}
.col.dark{background:var(--blue);color:#fff}
.col h4{font-size:13px;font-weight:400;letter-spacing:.3px;margin-bottom:12px}
.col ul{list-style:none}
.col li{position:relative;padding-left:17px;font-size:10.2px;line-height:15px;margin-bottom:8px}
.col li::before{content:"";position:absolute;left:3px;top:5px;width:4px;height:4px;border-radius:50%;background:var(--sky)}
.col.dark li::before{background:#fff}

/* testimonials */
.quote{top:2051px;width:232px;height:99px;border:1px solid #e9ecee;background:#fff;padding:27px 18px 0 44px;font-size:10.5px;line-height:15.5px;letter-spacing:.6px;color:var(--text)}
.quote::before{content:"\201C";position:absolute;left:17px;top:18px;font-family:var(--serif);font-size:24px;color:var(--blue)}
.person{top:2173px;display:flex;align-items:center;gap:14px}
.avatar{width:32px;height:32px;background:linear-gradient(135deg,#c9b6a8,#5b6672)}
.person b{display:block;font-weight:400;font-size:10.5px;letter-spacing:1px;color:var(--ink)}
.person i{font-style:normal;font-size:10.5px;color:var(--sky)}

/* inquiry form */
.form-panel{left:0;top:2271px;width:600px;height:736px;background:var(--teal)}
.form-photo{left:600px;top:2271px;width:600px;height:736px;background:radial-gradient(ellipse at 50% 45%,#d8b49c 0,#8c6553 22%,#2e2a2c 40%,#e5e8ea 62%,#f3f4f4 100%)}
.form-title{left:55px;top:2314px;font-family:var(--serif);font-weight:700;font-size:21px;letter-spacing:2px;color:#fff}
.form-rule{left:55px;top:2356px;width:44px;height:2px;background:#fff}
.form-sub{left:55px;font-family:var(--serif);font-weight:700;font-size:13px;letter-spacing:.6px;color:#fff}
.field{height:32px;border:1px solid #fff;border-radius:16px;padding-left:17px;font-size:8.5px;color:#fff;display:flex;align-items:center;width:239px}
.field.c1{left:55px}.field.c2{left:307px}
.radios{left:58px;top:2526px;display:flex;gap:16px;font-size:8px;color:#fff}
.radios span{display:flex;align-items:center;gap:5px}
.radios span.opt::before{content:"";width:7px;height:7px;border-radius:50%;background:#fff}
.textarea{left:55px;top:2803px;width:491px;height:98px;border:1px solid #fff;border-radius:10px;padding:19px 17px;font-size:8.5px;color:#fff}
.submit-btn{left:55px;top:2927px;width:152px;height:26px;font-size:9px}

/* news */
.news-img{top:3217px;width:232px;height:159px;background:linear-gradient(135deg,#eef1f3 0,#c7ced4 45%,#e7ebee 100%)}
.date{top:3199px;width:43px;height:39px;background:var(--blue);color:#fff;font-weight:700;font-size:13px;line-height:14px;text-align:center;padding-top:6px}
.news-text{top:3392px;width:232px}
.news-text h5{font-size:13px;font-weight:700;line-height:19px;color:var(--ink);letter-spacing:.2px}
.news-text p{margin-top:8px;font-size:10px;line-height:18px;color:var(--ink)}
.news-text span{display:block;margin-top:15px;font-size:10px;font-weight:700;letter-spacing:.8px;color:var(--blue)}

/* footer */
.footer{left:0;top:3563px;width:1200px;height:337px;background:var(--footer)}
.foot-bar{left:0;top:3900px;width:1200px;height:47px;background:var(--footer-deep)}
.foot-h{font-size:12px;font-weight:700;letter-spacing:.8px;color:#fff}
.quick{left:234px;top:3620px}
.quick ul{list-style:none;margin-top:10px}
.quick li{font-size:9px;color:#9ea2a6;line-height:21px;padding-left:2px}
.emp-btn{left:234px;top:3779px;width:154px;height:25px;background:var(--blue);color:#fff;font-size:8.5px;letter-spacing:.6px;display:flex;align-items:center;justify-content:center}
.foot-brand{left:450px;top:3596px;width:300px;display:flex;flex-direction:column;align-items:center;gap:6px}
.foot-brand .dot{width:12px;height:12px;border-radius:50%;background:var(--pale)}
.foot-brand .brand-name{color:#fff;font-size:13px}
.foot-about{left:450px;top:3680px;width:300px;text-align:center;font-size:8.5px;line-height:16px;color:#8f9499}
.social{top:3738px;width:18px;height:18px;border-radius:50%;background:#fff}
.news-h{left:450px;top:3805px;width:300px;text-align:center}
.email-in{left:470px;top:3837px;width:174px;height:24px;background:#2f2f2f;font-size:8.5px;color:#777;padding-left:10px;display:flex;align-items:center}
.subscribe{left:647px;top:3837px;width:81px;height:24px;background:#7fd3c9;color:#fff;font-size:8.5px;letter-spacing:.6px;display:flex;align-items:center;justify-content:center}
.contact-foot{right:232px;top:3620px;text-align:right}
.contact-foot p{font-size:9px;color:#9ea2a6;line-height:15px;padding-right:22px;position:relative}
.contact-foot svg{position:absolute;right:0;top:2px}
.copy{left:234px;top:3918px;font-size:8.5px;color:#8f9499}
.copy b{font-weight:400;color:var(--sky)}
.legal{right:232px;top:3918px;font-size:8.5px;color:#8f9499}
</style>
</head>
<body>

<!-- header -->
<div class="abs topbar"></div>
<div class="abs navband"></div>
<div class="abs brand-box"><span class="dot"></span><div class="brand-name">Harbor Light<br>Home</div></div>

<div class="abs contact-item phone">
  <svg width="16" height="16" viewBox="0 0 16 16"><path d="M3 2l3 0 1.5 3.5-2 1.2a8 8 0 0 0 3.8 3.8l1.2-2L14 10v3a1 1 0 0 1-1 1A11 11 0 0 1 2 3a1 1 0 0 1 1-1z" fill="none" stroke="#3276b5" stroke-width="1.3"/></svg>
  617-555-0142
</div>
<div class="abs contact-item" style="left:728px">
  <svg width="15" height="15" viewBox="0 0 16 16"><circle cx="8" cy="8" r="6.5" fill="none" stroke="#3276b5" stroke-width="1.5"/><path d="M8 4.5V8h3" fill="none" stroke="#3276b5" stroke-width="1.5"/></svg>
  <span>Monday - Friday<br>9:00am-5:00pm</span>
</div>
<div class="abs contact-item" style="left:845px">
  <svg width="13" height="16" viewBox="0 0 13 16"><path d="M6.5 15s5-5.2 5-8.8A5 5 0 0 0 1.5 6.2C1.5 9.8 6.5 15 6.5 15z" fill="none" stroke="#3276b5" stroke-width="1.3"/><circle cx="6.5" cy="6.3" r="1.8" fill="none" stroke="#3276b5" stroke-width="1.2"/></svg>
  <span>PO Box 418<br>Seabrook, MA 02100</span>
</div>

<nav class="abs nav"><span>HOME</span><span>ABOUT US</span><span>SERVICES</span><span>BLOG</span><span>CONTACT US</span></nav>
<div class="abs btn-pill inquiry-btn">MAKE AN INQUIRY</div>

<!-- hero -->
<section class="abs hero">
  <svg class="abs" style="left:0;top:0" width="1200" height="360">
    <polygon points="0,200 140,360 0,360" fill="#c2e8e2"/>
    <polygon points="1100,0 1200,0 1200,110" fill="#c2e8e2"/>
  </svg>
  <div class="abs hero-photo" role="img" aria-label="Portrait of the owner, a smiling nurse in a white coat with a stethoscope, seated in an office chair"></div>
  <div class="abs hero-eyebrow">WELCOME TO HARBOR LIGHT HOME</div>
  <h1 class="abs hero-title">Health &amp; Home<br>Services</h1>
  <div class="abs btn-pill hero-btn">GET IN TOUCH</div>
  <div class="abs arrow" style="left:234px">&#8249;</div>
  <div class="abs arrow" style="left:262px">&#8250;</div>
</section>

<!-- about -->
<section class="abs about"></section>
<div class="abs about-ring"><div class="about-photo" role="img" aria-label="Nurse caring for an elderly client seated at home"></div></div>
<div class="abs about-text">
  <div class="eyebrow">ABOUT US</div>
  <h2>Harbor Light Home Health Services is owned and operated by Claire Donovan.</h2>
  <p>Claire is a registered nurse and has been in the health care system since 2001. She has specialized in home care, cardiology, trauma and critical care. She invests in future caregivers and has taught for the nursing programs at <a>Eastbay University</a>, <a>Coastal Health Institute</a>, and <a>Marlowe College</a>.</p>
  <p>All Harbor Light Home caregivers have extensive background checks and training regarding HIPAA compliance. We individualize the care of our clients in order to provide the best care possible in their home. Harbor Light Home also ensures full access and understanding of client care at all times with a caregiver binder in the client's home at all times. This binder includes information on the client's care plan along with the notes from their caregivers. This will allow all caregivers and the client's family to have an understanding of the care being provided.</p>
</div>

<!-- services -->
<div class="abs shell" role="img" aria-label="Seashell emblem" style="left:576px;top:993px"></div>
<h2 class="abs sec-head" style="top:1032px">Services</h2>
<div class="abs rule" style="left:577px;top:1083px"></div>

<div class="abs why">
  <h3>Why Choose Home Care?</h3>
  <p style="margin-top:15px">Home care is a cost-effective option that allows clients the ability to receive one-on-one care in the comfort of their own home.</p>
  <p style="margin-top:16px">Home care also provides peace of mind to a client's family, near or far, without taking away a client's independence or privacy.</p>
  <h3 style="margin-top:33px">Care Schedule/Frequency</h3>
  <ul class="sched" style="margin-top:16px">
    <li>Harbor Light Home non-medical visits require a four hour minimum visit.</li>
    <li>There are no weekly minimum for medical or non-medical visits.</li>
    <li>Clients needing 24-hour care can save up 30% off of services by using a live-in caregiver. <i>(Live-in caregiver requires personal bedroom and bathroom.)</i></li>
  </ul>
  <h3 style="margin-top:36px">Payment Options</h3>
  <p style="margin-top:16px">Harbor Light Home currently accepts check for service payments (with plans for online payments late 2018.)</p>
</div>

<div class="abs map-title">Service Area Map</div>
<div class="abs map" role="img" aria-label="Map of the coastal towns covered by the service area, shaded in blue"></div>

<div class="abs cols">
  <div class="col light">
    <h4>SKILLED CARE SERVICES</h4>
    <ul>
      <li>Free Initial Nursing Assessment</li>
      <li>Medication Management</li>
      <li>Wound Care</li>
      <li>Injections</li>
      <li>Medical Care Assistance</li>
      <li>Transportation to Medical Appointments</li>
      <li>Care Plan Management</li>
    </ul>
  </div>
  <div class="col dark">
    <h4>NON-MEDICAL SERVICES</h4>
    <ul>
      <li>Live-In Care</li>
      <li>Respite Care</li>
      <li>Assisting with Daily Living Activities</li>
      <li>Meal Preparations</li>
      <li>Companionship</li>
      <li>Homemaking</li>
    </ul>
  </div>
  <div class="col light">
    <h4>CLIENT BENEFITS</h4>
    <ul>
      <li>Continuity of care with same caregiver for each client on a regular basis.</li>
      <li>Open communication with owner by phone or email.</li>
      <li>Ongoing communications to client's family by phone or email on a weekly basis <i>(if desired.)</i></li>
      <li>Streamlined payment process.</li>
    </ul>
  </div>
</div>

<!-- testimonials -->
<div class="abs shell" role="img" aria-label="Seashell emblem" style="left:576px;top:1905px"></div>
<h2 class="abs sec-head" style="top:1949px">What Our Clients Say</h2>

<div class="abs quote" style="left:234px">Lorem ipsum dolor sit amet, consectetur adipiscing elit. Ut consectetur facilisis ultricies."</div>
<div class="abs quote" style="left:486px">Lorem ipsum dolor sit amet, consectetur adipiscing elit. Ut consectetur facilisis ultricies."</div>
<div class="abs quote" style="left:736px">Lorem ipsum dolor sit amet, consectetur adipiscing elit. Ut consectetur facilisis ultricies."</div>

<div class="abs person" style="left:299px"><div class="avatar" role="img" aria-label="Client portrait"></div><div><b>Sam Ellery</b><i>CA</i></div></div>
<div class="abs person" style="left:551px"><div class="avatar" role="img" aria-label="Client portrait"></div><div><b>Sam Ellery</b><i>CA</i></div></div>
<div class="abs person" style="left:801px"><div class="avatar" role="img" aria-label="Client portrait"></div><div><b>Sam Ellery</b><i>CA</i></div></div>

<!-- inquiry form -->
<section class="abs form-panel"></section>
<div class="abs form-photo" role="img" aria-label="Portrait of the owner in a white coat wearing a turquoise necklace and a stethoscope"></div>
<h2 class="abs form-title">CARE INQUIRY FORM</h2>
<div class="abs form-rule"></div>
<div class="abs form-sub" style="top:2381px">Contact Information</div>
<div class="abs field c1" style="top:2432px">Contact First Name*</div>
<div class="abs field c2" style="top:2432px">Contact Last Name*</div>
<div class="abs field c1" style="top:2478px">Contact Phone Number*</div>
<div class="abs field c2" style="top:2478px">Contact Email Address*</div>
<div class="abs radios"><span>Best Way to Reach You*</span><span class="opt">By Phone</span><span class="opt">By Email</span></div>
<div class="abs form-sub" style="top:2563px">Client Information</div>
<div class="abs field c1" style="top:2614px">Client First Name*</div>
<div class="abs field c2" style="top:2614px">Client Last Name*</div>
<div class="abs field c1" style="top:2660px">Client Birthdate*</div>
<div class="abs field c2" style="top:2660px">Address*</div>
<div class="abs field c1" style="top:2707px">City</div>
<div class="abs field c2" style="top:2707px">State/Province</div>
<div class="abs field c1" style="top:2755px">Zip/Postal Code</div>
<div class="abs field c2" style="top:2755px">Country</div>
<div class="abs textarea">Please use this area to tell us more about the client and/or services that may be of interest to you. *</div>
<div class="abs btn-pill submit-btn">SUBMIT CARE INQUIRY</div>

<!-- news -->
<div class="abs shell" role="img" aria-label="Seashell emblem" style="left:576px;top:3067px"></div>
<h2 class="abs sec-head" style="top:3111px">News &amp; Articles</h2>

<div class="abs news-img" style="left:234px" role="img" aria-label="Doctor speaking with an elderly patient"></div>
<div class="abs news-img" style="left:486px" role="img" aria-label="Caregiver walking with a senior in a wheelchair outdoors"></div>
<div class="abs news-img" style="left:736px" role="img" aria-label="Doctor consulting a patient in a clinic"></div>
<div class="abs date" style="left:253px">16<br>Oct</div>
<div class="abs date" style="left:504px">16<br>Oct</div>
<div class="abs date" style="left:755px">16<br>Oct</div>

<div class="abs news-text" style="left:234px"><h5>Lorem ipsum dolor sit amet consectetur adipiscing elit.</h5><p>Ut consectetur facilisis ultricies. Suspendisse sed maximus orci. Praesent quis magna.</p><span>READ MORE</span></div>
<div class="abs news-text" style="left:486px"><h5>Lorem ipsum dolor sit amet consectetur adipiscing elit.</h5><p>Ut consectetur facilisis ultricies. Suspendisse sed maximus orci. Praesent quis magna.</p><span>READ MORE</span></div>
<div class="abs news-text" style="left:736px"><h5>Lorem ipsum dolor sit amet consectetur adipiscing elit.</h5><p>Ut consectetur facilisis ultricies. Suspendisse sed maximus orci. Praesent quis magna.</p><span>READ MORE</span></div>

<!-- footer -->
<footer class="abs footer"></footer>
<div class="abs foot-bar"></div>

<div class="abs quick">
  <div class="foot-h">QUICK LINKS</div>
  <ul><li>Home</li><li>About us</li><li>Services</li><li>Blog</li><li>Contact us</li></ul>
</div>
<div class="abs emp-btn">EMPLOYMENT APPLICATION</div>

<div class="abs foot-brand"><span class="dot"></span><div class="brand-name">Harbor Light Home</div></div>
<p class="abs foot-about">Harbor Light Home Health Services is owned and operated by Claire Donovan. Claire is a registered nurse and has been in the health care system since 2001.</p>
<div class="abs social" style="left:561px"></div>
<div class="abs social" style="left:589px"></div>
<div class="abs social" style="left:616px"></div>

<div class="abs foot-h news-h">REGISTER NEWSLETTER</div>
<div class="abs email-in">Your email address</div>
<div class="abs subscribe">SUBSCRIBE</div>

<div class="abs contact-foot">
  <div class="foot-h" style="margin-bottom:14px">CONTACT INFO</div>
  <p>PO Box 418<br>Seabrook, MA 02100<svg width="11" height="13" viewBox="0 0 13 16"><path d="M6.5 15s5-5.2 5-8.8A5 5 0 0 0 1.5 6.2C1.5 9.8 6.5 15 6.5 15z" fill="none" stroke="#3276b5" stroke-width="1.4"/></svg></p>
  <p style="margin-top:8px">Call Us<br>617-555-0142<svg width="11" height="11" viewBox="0 0 16 16"><path d="M3 2l3 0 1.5 3.5-2 1.2a8 8 0 0 0 3.8 3.8l1.2-2L14 10v3a1 1 0 0 1-1 1A11 11 0 0 1 2 3a1 1 0 0 1 1-1z" fill="none" stroke="#3276b5" stroke-width="1.5"/></svg></p>
  <div class="foot-h" style="margin-top:38px">AVAILABLE HOURS</div>
  <p style="margin-top:14px;padding-right:0">Monday-Friday &nbsp;9:00am-5:00pm</p>
</div>

<div class="abs copy">Copyright © 2019 <b>Harbor Light Home</b>. All Right Reserved.</div>
<div class="abs legal">Terms &amp; Condition &nbsp;&nbsp;|&nbsp;&nbsp; Privacy Policy</div>

</body>
</html>
```